We need a web page design for a new company called "Quarry". We provide an innovative music sharing mobile application that allows music listeners to share their music without paying for a monthly subscription. We would like to incorporate the attached logo and color scheme. The final design should communicate music gifting and sharing.

Industry/Entity Type

It Company

```html
<!DOCTYPE html>
<html lang="en">
<head>
<meta charset="utf-8">
<title>Quarry — own the music</title>
<link rel="stylesheet" href="https://fonts.googleapis.com/css2?family=Nunito:wght@400;600;700&family=Open+Sans:ital,wght@0,400;0,600;1,400&display=swap">
<style>
  :root{
    --green:#5ea817;
    --green-dark:#4a8c05;
    --green-light:#7cbc0f;
    --accent:#5aa30e;
    --ink:#333;
    --muted:#555;
    --soft:#666;
    --page:#f4f4f4;
    --panel:#ffffff;
    --line:#dcdcdc;
    --footer:#ececec;
  }
  *{box-sizing:border-box;margin:0;padding:0}
  html,body{width:997px;height:1200px;overflow:hidden}
  body{position:relative;background:var(--page);font-family:"Open Sans",Arial,sans-serif;color:var(--ink)}
  .heading{font-family:"Nunito",Arial,sans-serif}

  .site-header{position:absolute;left:0;top:0;width:997px;height:86px;background:var(--green)}
  .brand{position:absolute;left:113px;top:18px;display:flex;align-items:center;gap:8px;color:#fff}
  .brand-mark{width:34px;height:34px;border-radius:50%;background:#fff}
  .brand-name{font-family:"Nunito",sans-serif;font-weight:700;font-size:34px;line-height:1}
  .brand-tag{position:absolute;left:47px;top:38px;font-family:"Nunito",sans-serif;font-size:11px;letter-spacing:3px;color:#e6f3d2;white-space:nowrap}
  .main-nav{position:absolute;right:139px;top:48px;display:flex;gap:31px}
  .main-nav a{font-family:"Nunito",sans-serif;font-size:14px;color:#fff;text-decoration:none}
  .header-social{position:absolute;left:805px;top:19px;display:flex;gap:4px}
  .header-social span{width:13px;height:13px;border-radius:50%;background:#a7d46b}

  .hero{position:absolute;left:0;top:86px;width:997px;height:420px;
    background:radial-gradient(ellipse at 63% 40%,#8ccb1a 0%,var(--green-light) 35%,var(--green-dark) 100%)}
  .hero-arrow{position:absolute;top:150px}
  .hero-arrow.prev{left:46px}
  .hero-arrow.next{left:913px}
  .hero-copy{position:absolute;left:118px;top:105px;color:#fff;width:320px}
  .hero-copy h1{font-family:"Nunito",sans-serif;font-weight:600;font-size:37px;line-height:1;white-space:nowrap}
  .hero-copy h2{font-family:"Nunito",sans-serif;font-weight:400;font-size:22px;margin-top:9px;white-space:nowrap}
  .hero-copy p{font-size:10px;line-height:16px;margin-top:10px;color:#eef7e1;width:300px}
  .store-badges{position:absolute;left:118px;top:251px;display:flex;gap:10px}
  .store-badge{height:39px;background:#111;border:1px solid #777;border-radius:4px;color:#fff;display:flex;flex-direction:column;justify-content:center;padding:0 12px}
  .store-badge small{font-size:7px;letter-spacing:.5px}
  .store-badge b{font-family:"Open Sans",sans-serif;font-weight:600;font-size:17px;line-height:1}
  .store-badge.play{width:115px}
  .store-badge.shelf{width:118px}
  .hero-device{position:absolute;left:548px;top:28px;width:330px;height:364px;border-radius:40px 40px 0 0;
    background:linear-gradient(160deg,#e8e8e8 0%,#c9c9c9 30%,#2b3345 45%,#f0cdb9 80%,#e7b99e 100%)}

  .content-panel{position:absolute;left:93px;top:477px;width:811px;height:670px;background:var(--panel)}
  .intro{position:absolute;left:0;top:33px;width:811px;text-align:center}
  .intro h2{font-family:"Nunito",sans-serif;font-weight:400;font-size:27px;color:var(--muted)}
  .intro h3{font-family:"Nunito",sans-serif;font-weight:400;font-size:18px;color:var(--muted);margin-top:4px}
  .intro p{font-size:10px;line-height:16px;color:var(--soft);width:660px;margin:12px auto 0}

  .features{position:absolute;left:29px;top:206px;display:flex;gap:27px}
  .feature{position:relative;width:232px;height:100px}
  .feature-icon{position:absolute;left:0;top:0;width:83px;height:83px;border-radius:50%;border:2px solid #e2e2e2;display:flex;align-items:center;justify-content:center}
  .feature-body{position:absolute;left:93px;top:0;width:145px}
  .feature-body h4{font-family:"Nunito",sans-serif;font-weight:600;font-size:19px;color:var(--accent)}
  .feature-body p{font-size:10px;line-height:16px;color:var(--soft);margin-top:2px}
  .feature-body a{display:block;font-family:"Nunito",sans-serif;font-weight:700;font-size:11px;color:var(--ink);text-decoration:none;margin-top:2px}

  .divider{position:absolute;left:25px;top:356px;width:750px;height:1px;background:var(--line)}

  .testimonials-title{position:absolute;left:0;top:396px;width:811px;text-align:center;font-family:"Nunito",sans-serif;font-weight:400;font-size:23px;color:var(--ink)}
  .testimonial{position:absolute;top:445px;width:236px}
  .quote{position:relative;height:120px;border:1px solid var(--line);border-radius:2px;background:#fff;padding:17px 14px 0 20px;font-style:italic;font-size:9.5px;line-height:17px;color:var(--muted)}
  .quote::after{content:"";position:absolute;left:28px;bottom:-6px;width:10px;height:10px;background:#fff;border-right:1px solid var(--line);border-bottom:1px solid var(--line);transform:rotate(45deg)}
  .author{position:relative;height:50px;margin-top:16px}
  .author-photo{position:absolute;left:14px;top:0;width:40px;height:40px;border-radius:50%;background:linear-gradient(135deg,#c9a58c,#5a4436)}
  .author-name{position:absolute;left:62px;top:2px;font-family:"Nunito",sans-serif;font-size:11.5px;color:var(--accent)}
  .author-place{position:absolute;left:62px;top:20px;font-size:10px;color:var(--muted)}

  .site-footer{position:absolute;left:0;top:1147px;width:997px;height:53px;background:var(--footer)}
  .legal{position:absolute;left:136px;top:22px;font-size:10px;color:var(--ink)}
  .footer-social{position:absolute;left:802px;top:17px;display:flex;gap:7px}
  .footer-social span{width:18px;height:18px;border-radius:2px}
</style>
</head>
<body>

<header class="site-header">
  <div class="brand">
    <span class="brand-mark"></span>
    <span class="brand-name">Quarry</span>
    <span class="brand-tag">own the music</span>
  </div>
  <div class="header-social" aria-label="Social links">
    <span></span><span></span><span></span>
  </div>
  <nav class="main-nav">
    <a href="#">About</a><a href="#">Share Music</a><a href="#">Download</a><a href="#">Play Music</a><a href="#">Support</a>
  </nav>
</header>

<section class="hero">
  <svg class="hero-arrow prev" width="30" height="62" viewBox="0 0 30 62"><polyline points="28,1 2,31 28,61" fill="none" stroke="#dcefc2" stroke-width="1.5"/></svg>
  <svg class="hero-arrow next" width="30" height="62" viewBox="0 0 30 62"><polyline points="2,1 28,31 2,61" fill="none" stroke="#dcefc2" stroke-width="1.5"/></svg>
  <div class="hero-copy">
    <h1>Share Music to Friend</h1>
    <h2>Now gifting totally free</h2>
    <p>Vivamus porttitor purus nisi eleifend libero a tempus libero lectus feugiat felis Morbi diam mauris viverra in gravida eu mattis in ante Morbi eget arcu Morbi porta suscipit leo massa sodale</p>
  </div>
  <div class="store-badges">
    <a class="store-badge play"><small>GET IT ON</small><b>Playdeck</b></a>
    <a class="store-badge shelf"><small>Available on the</small><b>Appshelf</b></a>
  </div>
  <div class="hero-device" role="img" aria-label="Hand holding a smartphone showing the music player app"></div>
</section>

<main class="content-panel">
  <div class="intro">
    <h2>Vivamus porttitor purus nisi eleifend libero</h2>
    <h3>Suspendisse quam leo molestie sed luctus quis</h3>
    <p>Vivamus porttitor g purus nisi eleifend libero a tempus libero lectus feugiat felis Morbi diam mauris viverra in gravida eu mattis in ante Morbi eget arcu Morbi porta libero id ullamcorper nonummy nibh ligula pulvinar metus eget consectetuer augu Mauris vel lacus vitae felis vestibulum volutpat Etiam est nunc venenatis in tristique eu imperdiet ac nisl Cum sociis natoque</p>
  </div>

  <div class="features">
    <div class="feature">
      <div class="feature-icon">
        <svg width="38" height="38" viewBox="0 0 38 38"><path d="M13 8 L33 4 V26" fill="none" stroke="#5aa30e" stroke-width="4"/><line x1="13" y1="8" x2="13" y2="30" stroke="#5aa30e" stroke-width="4"/><ellipse cx="9" cy="31" rx="6" ry="5" fill="#5aa30e"/><ellipse cx="29" cy="27" rx="6" ry="5" fill="#5aa30e"/></svg>
      </div>
      <div class="feature-body"><h4>Share Music</h4><p>Libero lectus feugiat felis Morbi diam mauris viverra in gravida eu mattis in ante Morbi</p><a href="#">Learn More</a></div>
    </div>
    <div class="feature">
      <div class="feature-icon">
        <svg width="50" height="50" viewBox="0 0 50 50"><circle cx="25" cy="25" r="22" fill="none" stroke="#5aa30e" stroke-width="4"/><line x1="10" y1="10" x2="40" y2="40" stroke="#5aa30e" stroke-width="4"/><text x="25" y="34" text-anchor="middle" font-family="Nunito,sans-serif" font-weight="700" font-size="28" fill="#5aa30e">$</text></svg>
      </div>
      <div class="feature-body"><h4>Totally Free</h4><p>Libero lectus feugiat felis Morbi diam mauris viverra in gravida eu mattis in ante Morbi</p><a href="#">Learn More</a></div>
    </div>
    <div class="feature">
      <div class="feature-icon">
        <svg width="44" height="44" viewBox="0 0 44 44"><rect x="19" y="4" width="6" height="20" fill="#5aa30e"/><polygon points="10,20 34,20 22,33" fill="#5aa30e"/><polyline points="4,28 4,39 40,39 40,28" fill="none" stroke="#5aa30e" stroke-width="4"/></svg>
      </div>
      <div class="feature-body"><h4>Download Free</h4><p>Libero lectus feugiat felis Morbi diam mauris viverra in gravida eu mattis in ante Morbi</p><a href="#">Learn More</a></div>
    </div>
  </div>

  <div class="divider"></div>

  <h2 class="testimonials-title">Client Testimonials</h2>

  <article class="testimonial" style="left:35px">
    <p class="quote">Curabitur iaculis tempus eros Curabitur vel mi sit amet magna malesuada ultrices Ut nisi erat fermentum vel congue id euismod in elit Fusce ultricies orci ac feugiat suscipit leo massa sodales velit et scelerisque mi tortor at ipsum</p>
    <div class="author"><span class="author-photo" role="img" aria-label="Author portrait"></span><span class="author-name">Author Name</span><span class="author-place">Location Area, City</span></div>
  </article>
  <article class="testimonial" style="left:290px">
    <p class="quote">Curabitur iaculis tempus eros Curabitur vel mi sit amet magna malesuada ultrices Ut nisi erat fermentum vel congue id euismod in elit Fusce ultricies orci ac feugiat suscipit leo massa sodales velit et scelerisque mi tortor at ipsum</p>
    <div class="author"><span class="author-photo" role="img" aria-label="Author portrait"></span><span class="author-name">Author Name</span><span class="author-place">Location Area, City</span></div>
  </article>
  <article class="testimonial" style="left:543px">
    <p class="quote">Curabitur iaculis tempus eros Curabitur vel mi sit amet magna malesuada ultrices Ut nisi erat fermentum vel congue id euismod in elit Fusce ultricies orci ac feugiat suscipit leo massa sodales velit et scelerisque mi tortor at ipsum</p>
    <div class="author"><span class="author-photo" role="img" aria-label="Author portrait"></span><span class="author-name">Author Name</span><span class="author-place">Location Area, City</span></div>
  </article>
</main>

<footer class="site-footer">
  <p class="legal">© 2014 Company Name &nbsp;All right reserved &nbsp;| &nbsp;Term of Use &nbsp;| &nbsp;Privacy Policy</p>
  <div class="footer-social" aria-label="Social links">
    <span style="background:#3b5a9a"></span><span style="background:#4fb1e3"></span><span style="background:#1a6aa5"></span>
  </div>
</footer>

</body>
</html>
```